Cleaning service website design

We need a new nice web design(logo will be the same) for a new cleaning service Company:

Informations about Company and logo you can take from flyers in attachments.

This is a cleaning service Company which have simple rules and we would like to show that(in checklist form) on website:

- What we do and that we're Cleaning Green

- Why us?

- How much(our pricing is simple)

Also we would like to communicate with clients by some nice/big pictures on website and the most important thing is our phone number and short/fast Freestimate.

Also there should be some space for description about our Company.

Generally all information on main page can be short: about us, about service(what we do), last reviews, tips (for example: Tip of the week) and other can be some introduction to subpage where will be more information.

There will be few subpages like: About us, About our service, Photos(Before and after), Reviews , Tips, FAQ, Contact, Looking for a Job? - most of them will be just text so you can project just one example.

```html
<!DOCTYPE html>
<html lang="en">
<head>
<meta charset="utf-8">
<title>Tidy Nest – Home Cleaning</title>
<link href="https://fonts.googleapis.com/css2?family=Open+Sans:ital,wght@0,400;0,600;0,700;1,400;1,600&family=Kaushan+Script&display=swap" rel="stylesheet">
<style>
:root{
  --green:#5fb52e;
  --green-dark:#3e8a1a;
  --green-light:#a8dc6a;
  --blue:#1e63b0;
  --blue-dark:#123f7a;
  --sky:#e9f3fb;
  --text:#4a4a4a;
  --muted:#8a8a8a;
  --white:#ffffff;
}
*{box-sizing:border-box;margin:0;padding:0}
html,body{width:713px;height:1200px;overflow:hidden}
body{font-family:"Open Sans",Arial,sans-serif;color:var(--text);background:var(--white);font-size:7px;line-height:1.35;position:relative}
.script{font-family:"Kaushan Script",cursive}

.site-header{position:absolute;top:0;left:0;width:713px;height:92px}
.brand{position:absolute;left:60px;top:8px;display:flex;align-items:center;gap:8px}
.brand-dot{width:40px;height:40px;border-radius:50%;background:var(--green)}
.brand-name{font-size:22px;font-weight:700;color:var(--green)}
.call{position:absolute;right:60px;top:14px;text-align:right}
.call .tag{font-family:"Kaushan Script",cursive;font-size:26px;color:var(--blue);line-height:1}
.call .phone{font-size:18px;font-weight:700;color:var(--green);margin-top:4px;display:flex;align-items:center;gap:6px;justify-content:flex-end}
.call .phone span.lbl{font-family:"Kaushan Script",cursive;font-weight:400}

.main-nav{position:absolute;top:98px;left:94px;display:flex;gap:4px}
.main-nav a{font-size:8px;color:var(--muted);text-decoration:none;padding:4px 9px;border-radius:12px}
.main-nav a.active{background:var(--green);color:var(--white);font-weight:600}

.hero{position:absolute;top:125px;left:60px;width:593px;height:230px;background:linear-gradient(180deg,#ffffff 0%,var(--sky) 100%);border-radius:4px;overflow:hidden}
.hero-title{position:absolute;left:48px;top:90px;color:var(--green);font-family:"Kaushan Script",cursive;font-size:34px;line-height:1}
.hero-title small{display:block;font-size:24px;color:var(--blue);margin-left:28px}
.hero-title em{font-style:normal;font-size:40px;display:block;color:var(--green)}
.hero-photo{position:absolute;right:40px;top:10px;width:260px;height:220px;background:linear-gradient(180deg,#dbe9f3,#b9cfe0)}
.hero-arrow{position:absolute;top:95px;width:26px;height:26px;border-radius:50%;background:var(--green)}
.hero-arrow.prev{left:-4px}.hero-arrow.next{right:-4px}
.hero-arrow svg{display:block}
.dots{position:absolute;top:396px;left:340px;display:flex;gap:4px}
.dots i{width:7px;height:7px;border-radius:50%;background:#c8c8c8}
.dots i:first-child{background:var(--green)}

.welcome{position:absolute;top:408px;left:60px;width:593px}
.welcome h1{font-size:22px;font-weight:400;color:var(--green)}
.welcome h1 span{color:var(--blue)}
.welcome-body{display:flex;gap:12px;margin-top:8px}
.owners{width:118px;height:120px;flex:none;background:linear-gradient(180deg,#9ab8d0,#5d7f99)}
.welcome-text p{margin-bottom:6px;font-size:7px}
.welcome-text .lead{font-style:italic;color:var(--blue);font-size:10px;margin-bottom:4px}
.welcome-text .sign{font-style:italic;font-weight:600}

.features{position:absolute;top:600px;left:55px;width:603px;display:flex;gap:10px}
.card{flex:1;background:var(--white);border:1px solid #d9e2ea;height:240px}
.card h2{background:var(--blue);color:var(--white);text-align:center;font-size:11px;font-weight:600;padding:5px 0}
.card .pic{height:70px;margin:6px}
.card ul{list-style:none;padding:0 10px}
.card li{display:flex;gap:5px;align-items:flex-start;margin-bottom:4px;font-size:7px}
.tick{flex:none;width:8px;height:8px;margin-top:1px}
.pricing{flex:1;background:linear-gradient(180deg,var(--green-light),var(--green));border-radius:6px;height:240px;color:var(--white);padding:12px 12px;text-align:center}
.pricing h2{font-size:22px;font-weight:400}
.pricing h2 .script{font-size:30px;display:block;margin:-6px 0 6px 40px}
.pricing ul{list-style:none;text-align:left;margin-top:4px}
.pricing li{font-size:9px;margin-bottom:5px;display:flex;gap:5px;font-weight:600}
.pricing li b{color:var(--blue-dark)}
.pricing .note{font-style:italic;color:var(--blue-dark);font-size:9px;margin:6px 0}
.pricing .reg{font-size:8px;font-style:italic}

.lower{position:absolute;top:852px;left:0;width:713px;height:305px;background:linear-gradient(180deg,var(--green-light) 0%,var(--green) 100%)}
.reviews{position:absolute;left:60px;top:10px;width:300px;color:var(--white)}
.reviews h2,.tip h2{font-family:"Kaushan Script",cursive;font-weight:400;font-size:26px;color:var(--blue-dark)}
.reviews .intro{font-size:7px;margin:4px 0 8px}
.review{display:flex;gap:8px;background:var(--blue);border-radius:4px;padding:8px;margin-bottom:8px}
.review .avatar{width:46px;height:46px;flex:none;background:linear-gradient(180deg,#c7d5e2,#8aa0b4)}
.review p{font-size:7px}
.review a{color:var(--white);font-weight:700;font-size:7px;display:inline-block;margin-top:3px}
.tip{position:absolute;left:410px;top:10px;width:245px;color:var(--white)}
.tip-box{background:var(--blue);border-radius:4px;padding:10px;margin-top:6px;height:170px}
.tip-box p{font-size:7px;margin-bottom:6px}

.site-footer{position:absolute;top:1157px;left:0;width:713px;height:43px;background:var(--blue-dark);color:var(--white)}
.site-footer nav{display:flex;gap:10px;padding:8px 0 0 62px}
.site-footer a{color:var(--white);text-decoration:none;font-size:6px}
.site-footer .copy{padding-left:62px;margin-top:6px;font-size:5px;color:#b8c8e0}
</style>
</head>
<body>

<header class="site-header">
  <div class="brand"><span class="brand-dot"></span><span class="brand-name">Tidy Nest</span></div>
  <div class="call">
    <div class="tag">It's simple...</div>
    <div class="phone">
      <svg width="14" height="14" viewBox="0 0 24 24"><path fill="#5fb52e" d="M6.6 10.8a15 15 0 006.6 6.6l2.2-2.2a1 1 0 011-.25 11 11 0 003.5.56 1 1 0 011 1V20a1 1 0 01-1 1A17 17 0 013 4a1 1 0 011-1h3.5a1 1 0 011 1 11 11 0 00.56 3.5 1 1 0 01-.25 1z"/></svg>
      <span class="lbl">Call today!</span> 555-014-2290
    </div>
  </div>
</header>

<nav class="main-nav">
  <a class="active" href="#">Home</a><a href="#">About Us</a><a href="#">Services</a><a href="#">Gallery</a><a href="#">Reviews</a><a href="#">Tips</a><a href="#">FAQ</a><a href="#">Looking for a Job?</a><a href="#">Contact</a>
</nav>

<section class="hero">
  <div class="hero-title">Affordably<small>making your life</small><em>Simpler</em></div>
  <div class="hero-photo" role="img" aria-label="Two cleaners in uniforms with a cleaning cart, mop and broom"></div>
  <span class="hero-arrow prev"><svg width="26" height="26" viewBox="0 0 26 26"><path d="M15 7l-6 6 6 6" stroke="#fff" stroke-width="2.5" fill="none"/></svg></span>
  <span class="hero-arrow next"><svg width="26" height="26" viewBox="0 0 26 26"><path d="M11 7l6 6-6 6" stroke="#fff" stroke-width="2.5" fill="none"/></svg></span>
</section>
<div class="dots"><i></i><i></i><i></i></div>

<section class="welcome">
  <h1>Welcome <span>to Our Website</span></h1>
  <div class="welcome-body">
    <div class="owners" role="img" aria-label="Photo of the company owners"></div>
    <div class="welcome-text">
      <p class="lead">It's about caring, not just cleaning.</p>
      <p>Having personally experienced the struggle of finding quality maid service for our home, we set out to make it simpler for families in the area. Our goal is to provide caring, consistent and reliable house cleaning to every customer we serve.</p>
      <p>We pride ourselves on delivering the best possible customer experience and on providing outstanding healthy home cleaning to this vibrant and rapidly growing community.</p>
      <p>We are passionate about making a difference in the community and having Tidy Nest become synonymous with reliable and dependable housekeeping services. With local focus and attention to quality and service we believe the families we serve can be confident they are receiving the best and most reliable service around.</p>
      <p>We are proud to serve the communities of Westbrook, Linden and Hallow Bay.</p>
      <p class="sign">~ Anna &amp; Mark</p>
    </div>
  </div>
</section>

<section class="features">
  <article class="card">
    <h2>What we do</h2>
    <div class="pic" role="img" aria-label="Spotless bathroom with a clean tub and sink" style="background:linear-gradient(180deg,#d7cdbf,#9e8b73)"></div>
    <ul>
      <li><svg class="tick" viewBox="0 0 10 10"><path d="M1 5l3 3 5-7" stroke="#5fb52e" stroke-width="2" fill="none"/></svg>Thoroughly clean your bathrooms, kitchen, bedrooms and living areas</li>
      <li><svg class="tick" viewBox="0 0 10 10"><path d="M1 5l3 3 5-7" stroke="#5fb52e" stroke-width="2" fill="none"/></svg>Mop or vacuum your floors</li>
      <li><svg class="tick" viewBox="0 0 10 10"><path d="M1 5l3 3 5-7" stroke="#5fb52e" stroke-width="2" fill="none"/></svg>Dust surfaces</li>
      <li><svg class="tick" viewBox="0 0 10 10"><path d="M1 5l3 3 5-7" stroke="#5fb52e" stroke-width="2" fill="none"/></svg>Collect garbage</li>
      <li><svg class="tick" viewBox="0 0 10 10"><path d="M1 5l3 3 5-7" stroke="#5fb52e" stroke-width="2" fill="none"/></svg>Make beds</li>
    </ul>
  </article>
  <article class="pricing">
    <h2>Pricing is <span class="script">simple,</span></h2>
    <ul>
      <li><b>&#10003;</b>$79 for homes less than 1000 sq ft</li>
      <li><b>&#10003;</b>$89 for homes less than 2000 sq ft</li>
      <li><b>&#10003;</b>$99 for homes less than 3000 sq ft</li>
    </ul>
    <p class="note">If your home is larger than 3000 sq ft please call for a quote</p>
    <p class="reg">*rates are for regular service*</p>
  </article>
  <article class="card">
    <h2>Why choose us?</h2>
    <div class="pic" role="img" aria-label="Two smiling cleaners in uniform" style="background:linear-gradient(180deg,#cfdbe6,#8ea6bb)"></div>
    <ul>
      <li><svg class="tick" viewBox="0 0 10 10"><path d="M1 5l3 3 5-7" stroke="#5fb52e" stroke-width="2" fill="none"/></svg>Owners Present at Every Cleaning</li>
      <li><svg class="tick" viewBox="0 0 10 10"><path d="M1 5l3 3 5-7" stroke="#5fb52e" stroke-width="2" fill="none"/></svg>Locally Owned &amp; Operated</li>
      <li><svg class="tick" viewBox="0 0 10 10"><path d="M1 5l3 3 5-7" stroke="#5fb52e" stroke-width="2" fill="none"/></svg>Reliable &amp; Affordable</li>
      <li><svg class="tick" viewBox="0 0 10 10"><path d="M1 5l3 3 5-7" stroke="#5fb52e" stroke-width="2" fill="none"/></svg>All Supplies Provided</li>
      <li><svg class="tick" viewBox="0 0 10 10"><path d="M1 5l3 3 5-7" stroke="#5fb52e" stroke-width="2" fill="none"/></svg>Green Cleaning</li>
      <li><svg class="tick" viewBox="0 0 10 10"><path d="M1 5l3 3 5-7" stroke="#5fb52e" stroke-width="2" fill="none"/></svg>Pet Friendly</li>
      <li><svg class="tick" viewBox="0 0 10 10"><path d="M1 5l3 3 5-7" stroke="#5fb52e" stroke-width="2" fill="none"/></svg>No Contracts</li>
    </ul>
  </article>
</section>

<section class="lower">
  <div class="reviews">
    <h2>last reviews</h2>
    <p class="intro">Our clients tell it best. Here is what families say after their very first clean with our friendly team.</p>
    <div class="review">
      <div class="avatar" role="img" aria-label="Customer portrait"></div>
      <div><p>Our house has never looked this good. The team arrived on time, worked quickly and left every room fresh and bright.</p><a href="#">Read more</a></div>
    </div>
    <div class="review">
      <div class="avatar" role="img" aria-label="Customer portrait"></div>
      <div><p>Simple pricing, no surprises and truly careful people. We booked regular service the same week and love it.</p><a href="#">Read more</a></div>
    </div>
  </div>
  <div class="tip">
    <h2>Tip of the week</h2>
    <div class="tip-box">
      <p>Keep a small caddy of green cleaners under each sink. A quick wipe after use stops soap scum from building up.</p>
      <p>Mix warm water with a splash of vinegar for streak free windows and mirrors, then dry with a soft cloth.</p>
      <p>Open windows for ten minutes each morning to refresh the air and keep your home smelling clean all day.</p>
    </div>
  </div>
</section>

<footer class="site-footer">
  <nav><a href="#">Home</a><a href="#">About Us</a><a href="#">Services</a><a href="#">Gallery</a><a href="#">Reviews</a><a href="#">Tips</a><a href="#">FAQ</a><a href="#">Looking for a Job?</a><a href="#">Contact</a></nav>
  <p class="copy">© Tidy Nest. All rights reserved.</p>
</footer>

</body>
</html>
```